need a clean, modern job advertisement designed for social media (Facebook & Instagram).

The post is to advertise two positions:
• Leading Hand Boilermaker
• Dragline Fitter
We want the design to match our KRT Plant Services branding: blue, white, strong, professional, mining-industry style.
What the design should include:
Bold headline: “WE’RE HIRING”
Sub-headline: “Leading Hand Boilermaker & Dragline Fitter”
Key points:
• Bowen Basin based
• Dragline & shovel maintenance
• Great pay + long-term work
• Locally owned & operated
KRT logo placed cleanly
Space for 1–2 images (boilermaking or dragline work)
Design style:
Strong and industrial
Blue/white colour scheme
Easy to read at a glance
Suitable for a square 1080×1080 design

```html
<!DOCTYPE html>
<html lang="en">
<head>
<meta charset="utf-8">
<title>KRT Plant Services – We're Hiring social posts</title>
<link rel="stylesheet" href="https://fonts.googleapis.com/css2?family=Exo+2:ital,wght@1,800;1,900&family=Rajdhani:wght@600;700&family=Roboto+Condensed:ital,wght@0,500;1,700&display=swap">
<style>
  :root {
    --board: #e2e2e2;
    --ink: #141414;
    --black: #151617;
    --navy: #0f1c2e;
    --navy-deep: #0a1422;
    --blue: #1565ff;
    --sky: #3fb4f2;
    --white: #ffffff;
    --silver: #b9bcc0;
    --band-grey: #e9e9e9;
  }
  * { margin: 0; padding: 0; box-sizing: border-box; }
  html, body { width: 1200px; height: 1116px; overflow: hidden; background: var(--board); }
  .board { position: relative; width: 1200px; height: 1116px; }

  .ad { position: absolute; width: 440px; height: 440px; overflow: hidden; background: var(--navy); }
  .ad > svg { position: absolute; inset: 0; }
  .ad--one   { left: 124px; top: 66px; }
  .ad--two   { left: 631px; top: 66px; }
  .ad--three { left: 124px; top: 590px; }
  .ad--four  { left: 631px; top: 590px; }

  .sample-label {
    position: absolute; font: 700 20px/1 'Rajdhani', sans-serif;
    letter-spacing: 1.5px; color: var(--ink);
  }

  .t { position: absolute; white-space: nowrap; }
  .were { font: italic 900 40px/1 'Exo 2', sans-serif; color: var(--white); }
  .hiring {
    font: italic 900 78px/1 'Exo 2', sans-serif; padding-right: 8px;
    background: linear-gradient(180deg, #6fd0ff 0%, #2d9ae8 38%, #ffffff 52%, #cfd2d6 70%, #8d9196 100%);
    -webkit-background-clip: text; background-clip: text; color: transparent;
  }
  .hiring--solid { background: none; color: var(--blue); }
  .role { font: italic 700 23px/1 'Roboto Condensed', sans-serif; color: var(--sky); }
  .role--stack { font: 500 22px/1.18 'Roboto Condensed', sans-serif; color: var(--white); font-style: normal; white-space: normal; }
  .role--dark { color: var(--ink); font-size: 20px; }
  .role--light { color: var(--white); font-size: 19px; }

  .points { position: absolute; list-style: none; font: 700 15px/1 'Rajdhani', sans-serif; color: var(--white); }
  .points li { position: relative; padding-left: 0; }
  .points li::before {
    content: ''; position: absolute; left: -15px; top: 50%; margin-top: -4px;
    border-left: 6px solid var(--sky); border-top: 4px solid transparent; border-bottom: 4px solid transparent;
  }
  .points--lg { font-size: 17px; }

  .apply {
    position: absolute; display: flex; align-items: center; justify-content: center;
    background: var(--blue); color: var(--white);
    font: 700 15px/1 'Rajdhani', sans-serif; letter-spacing: 1.5px;
  }
  .apply--slant { clip-path: polygon(5% 0, 100% 0, 95% 100%, 0 100%); font-size: 17px; }

  .brand {
    position: absolute; display: flex; align-items: center; gap: 6px;
    font: 700 17px/1.05 'Rajdhani', sans-serif; color: var(--white);
  }
  .brand__dot { width: 12px; height: 12px; border-radius: 50%; background: var(--sky); flex: none; }
</style>
</head>
<body>
<div class="board">
  <svg width="0" height="0" style="position:absolute">
    <defs>
      <linearGradient id="photo-weld" x1="0" y1="0" x2="1" y2="1">
        <stop offset="0" stop-color="#1d2a55"/><stop offset=".45" stop-color="#3a4a8a"/><stop offset="1" stop-color="#1a1c2a"/>
      </linearGradient>
      <linearGradient id="photo-sparks" x1="0" y1="0" x2="1" y2="1">
        <stop offset="0" stop-color="#2a2522"/><stop offset=".5" stop-color="#4a3420"/><stop offset="1" stop-color="#1e1a18"/>
      </linearGradient>
      <linearGradient id="panel-navy" x1="0" y1="0" x2="0" y2="1">
        <stop offset="0" stop-color="#14243b"/><stop offset="1" stop-color="#0a1422"/>
      </linearGradient>
    </defs>
  </svg>

  <!-- Layout one -->
  <section class="ad ad--one">
    <svg viewBox="0 0 440 440" width="440" height="440">
      <rect width="440" height="440" fill="url(#panel-navy)"/>
      <rect width="440" height="112" fill="var(--black)"/>
      <polygon points="300,300 440,300 440,440 210,440" fill="#17191c"/>
      <polygon points="0,112 142,112 256,283 0,283" fill="url(#photo-sparks)" role="img" aria-label="Photo: boilermaker grinding with sparks inside a dragline bucket"/>
      <polygon points="166,127 440,127 440,300 278,300" fill="url(#photo-weld)" role="img" aria-label="Photo: welder in hood working on dragline steel"/>
      <polyline points="142,112 256,283" stroke="var(--sky)" stroke-width="3" fill="none"/>
      <polyline points="166,127 440,127" stroke="#8fa7c4" stroke-width="2" fill="none"/>
      <rect x="0" y="283" width="256" height="4" fill="#1e4f9a"/>
      <polyline points="278,300 200,440" stroke="#2b3a52" stroke-width="2" fill="none"/>
    </svg>
    <div class="t were" style="left:24px;top:20px;">We're</div>
    <div class="t hiring" style="left:150px;top:2px;">HIRING</div>
    <div class="t role" style="left:22px;top:78px;">Leading Hand Boilermaker &amp; Dragline Fitter</div>
    <ul class="points" style="left:38px;top:306px;">
      <li style="height:21px">Bowen Basin based</li>
      <li style="height:21px">Dragline &amp; shovel maintenance</li>
      <li style="height:21px">Great pay + long-term work</li>
      <li style="height:21px">Locally owned &amp; operated</li>
    </ul>
    <div class="apply" style="left:27px;top:397px;width:99px;height:25px;">APPLY NOW</div>
    <div class="brand" style="left:308px;top:356px;"><span class="brand__dot"></span><span>KRT Plant<br>Services</span></div>
  </section>

  <!-- Layout two -->
  <section class="ad ad--two">
    <svg viewBox="0 0 440 440" width="440" height="440">
      <rect width="440" height="440" fill="url(#panel-navy)"/>
      <polygon points="295,3 440,3 440,218 195,218" fill="url(#photo-weld)" role="img" aria-label="Photo: welder in hood working on dragline steel"/>
      <polygon points="196,228 440,228 440,440 297,440" fill="url(#photo-sparks)" role="img" aria-label="Photo: boilermaker grinding with sparks inside a dragline bucket"/>
      <polyline points="295,0 193,220 440,220" stroke="#c8ccd2" stroke-width="2.5" fill="none"/>
      <polyline points="292,0 190,220" stroke="var(--sky)" stroke-width="2" fill="none"/>
      <rect x="292" y="0" width="148" height="4" fill="var(--sky)"/>
      <rect x="196" y="225" width="244" height="2" fill="var(--sky)"/>
      <rect x="19" y="140" width="165" height="1.5" fill="var(--blue)"/>
      <rect x="19" y="226" width="165" height="1.5" fill="var(--blue)"/>
    </svg>
    <div class="t were" style="left:26px;top:17px;">WE'RE</div>
    <div class="t hiring hiring--solid" style="left:18px;top:56px;font-size:78px;transform:scaleX(.8);transform-origin:left;">HIRING</div>
    <div class="t role role--stack" style="left:19px;top:146px;width:200px;">LEADING HAND<br>BOILERMAKER &amp;<br>DRAGLINE FITTER</div>
    <ul class="points" style="left:40px;top:250px;line-height:19px;">
      <li style="margin-bottom:4px">Bowen Basin based</li>
      <li style="margin-bottom:4px">Dragline &amp; shovel<br>maintenance</li>
      <li style="margin-bottom:4px">Great pay +<br>long-term work</li>
      <li>Locally owned &amp; operated</li>
    </ul>
    <div class="apply apply--slant" style="left:25px;top:396px;width:126px;height:21px;">APPLY NOW</div>
    <div class="brand" style="left:344px;top:376px;font-size:15px;"><span class="brand__dot"></span><span>KRT Plant<br>Services</span></div>
  </section>

  <!-- Layout three -->
  <section class="ad ad--three">
    <svg viewBox="0 0 440 440" width="440" height="440">
      <rect width="440" height="440" fill="#1a2230"/>
      <rect y="318" width="440" height="122" fill="var(--navy)"/>
      <rect y="149" width="440" height="24" fill="var(--band-grey)"/>
      <rect y="173" width="440" height="3" fill="var(--sky)"/>
      <polygon points="0,176 217,176 184,318 0,318" fill="url(#photo-sparks)" role="img" aria-label="Photo: boilermaker grinding with sparks inside a dragline bucket"/>
      <polygon points="223,176 440,176 440,318 190,318" fill="url(#photo-weld)" role="img" aria-label="Photo: welder in hood working on dragline steel"/>
      <rect y="318" width="440" height="3" fill="#1e4f9a"/>
    </svg>
    <div class="brand" style="left:26px;top:60px;font-size:22px;"><span class="brand__dot"></span><span>KRT Plant<br>Services</span></div>
    <div class="t were" style="left:294px;top:16px;">WE'RE</div>
    <div class="t hiring" style="left:160px;top:40px;font-size:100px;transform:scaleX(.76);transform-origin:left;">HIRING</div>
    <div class="t role role--dark" style="left:21px;top:151px;">LEADING HAND BOILERMAKER &amp; DRAGLINE FITTER</div>
    <ul class="points points--lg" style="left:38px;top:335px;">
      <li style="height:24px">Bowen Basin based</li>
      <li style="height:24px">Dragline &amp; shovel maintenance</li>
      <li style="height:24px">Great pay + long-term work</li>
      <li style="height:24px">Locally owned &amp; operated</li>
    </ul>
    <div class="apply apply--slant" style="left:291px;top:375px;width:122px;height:22px;">APPLY NOW</div>
  </section>

  <!-- Layout four -->
  <section class="ad ad--four">
    <svg viewBox="0 0 440 440" width="440" height="440">
      <rect width="440" height="440" fill="url(#panel-navy)"/>
      <rect width="440" height="78" fill="var(--black)"/>
      <rect y="78" width="440" height="26" fill="var(--sky)"/>
      <polygon points="0,104 171,104 283,281 0,281" fill="url(#photo-sparks)" role="img" aria-label="Photo: boilermaker grinding with sparks inside a dragline bucket"/>
      <polygon points="186,104 440,104 440,281 301,281" fill="url(#photo-weld)" role="img" aria-label="Photo: welder in hood working on dragline steel"/>
      <polyline points="171,104 283,281" stroke="var(--sky)" stroke-width="3" fill="none"/>
      <polyline points="186,104 301,281" stroke="#0e1624" stroke-width="4" fill="none"/>
      <rect y="281" width="440" height="3" fill="#1e4f9a"/>
    </svg>
    <div class="t were" style="left:26px;top:20px;">We're</div>
    <div class="t hiring" style="left:151px;top:1px;">HIRING</div>
    <div class="t role role--light" style="left:22px;top:81px;">LEADING HAND BOILERMAKER &amp; DRAGLINE FITTER</div>
    <ul class="points points--lg" style="left:39px;top:295px;">
      <li style="height:23.5px">Bowen Basin based</li>
      <li style="height:23.5px">Dragline &amp; shovel maintenance</li>
      <li style="height:23.5px">Great pay + long-term work</li>
      <li style="height:23.5px">Locally owned &amp; operated</li>
    </ul>
    <div class="brand" style="left:305px;top:328px;"><span class="brand__dot"></span><span>KRT Plant<br>Services</span></div>
    <div class="apply apply--slant" style="left:159px;top:402px;width:121px;height:20px;">APPLY NOW</div>
  </section>

  <div class="sample-label" style="left:124px;top:524px;">SAMPLE 1</div>
  <div class="sample-label" style="left:631px;top:524px;">SAMPLE 2</div>
  <div class="sample-label" style="left:124px;top:1048px;">SAMPLE 3</div>
  <div class="sample-label" style="left:631px;top:1048px;">SAMPLE 4</div>
</div>
</body>
</html>
```